Wordpress Design Project

Hi,

I would like a more modern colourful design doing for my website Zyl Pando (www.zy%lpando.com - remove percentage). But I do still want to keep the same sort of colors, just maybe lighter. More interesting.

I want the inside pages to NOT all look the same with just boring text.

I want the site to look more appealing and maybe a new logo.
Updates

I would like to mention I would prefer to keep the same logo after rethinking it (possibly a slight refresh of the logo if you feel its a good idea) and the same color scheme as at present.

Saves us rebranding a lot of our apps, tools online ads etc.

Also I thought it is worth mentioning we have 2 parts to the site. The front end and the logged in area. It would be good if when making the front end you keep in mind the back end at http://p.zy%lpando.com (remove percentage). We can only edit this limitedly (can edit the entire footer, the logo and full CSS of it). Would be good if we could make sure the header and footer can be used on the back end as well maybe to make it match.

I also want layouts making not just for the homepage. Obviously every page will basically be the same but I don't want all the other pages to just be 'text' and no real layout.

You can see out main pages on the website at the moment, I want those other pages to be laid out nice and differently as well. For example the testimonials page could be more interesting with speech bubbles and pictures of each person (just use placeholders). The affiliates page could be a description and then a nice fancy list of features why to join etc. 

Nothing overly complicated but I think it makes the whole site seem a lot better.

Target Market(s)

Affiliate Marketing. International.

Requirements
Must have
• Needs to be more room for links across the navigation at the top, also sub menus (at present we have a lot of pages which are hidden deep within other pages).
Nice to have
• Lists of features for advertisers and affiliates on the homepage part.

Menu items and buttons have nice hover over effects.

I want to get across on our pages all the different unique features we have.

Maybe some kind of slider which has past offer logos in, just use example logos.

```html
<!DOCTYPE html>
<html lang="en">
<head>
<meta charset="utf-8">
<title>Zyl Pando – International CPA Affiliate Network</title>
<link href="https://fonts.googleapis.com/css2?family=Questrial&display=swap" rel="stylesheet">
<style>
:root{
  --orange:#ff6a00;
  --orange-dark:#e35400;
  --blue:#1f7fd8;
  --blue-dark:#0e5aa8;
  --ink:#333333;
  --grey:#8a8a8a;
  --light:#f2f0ec;
  --panel:#f6f6f6;
  --dark:#1b1b1b;
  --white:#ffffff;
  --card-line:#dddddd;
}
*{margin:0;padding:0;box-sizing:border-box}
html,body{width:1200px;height:1102px;overflow:hidden}
body{position:relative;background:var(--white);font-family:"Questrial",Arial,sans-serif;color:var(--ink)}
.abs{position:absolute}

/* header */
.site-header{left:0;top:0;width:1200px;height:86px;background:var(--white)}
.brand{left:222px;top:14px;display:flex;align-items:center;gap:8px}
.brand-mark{width:34px;height:34px;border-radius:50%;background:var(--orange)}
.brand-name{font-size:36px;color:#3a3a3a;letter-spacing:1px}
.brand-tagline{left:316px;top:54px;font-size:11px;color:#555}
.auth{top:16px;height:18px;border-radius:9px;color:var(--white);font-size:9px;font-weight:bold;text-align:center;line-height:18px;font-family:Arial,sans-serif}
.auth.sign-in{left:752px;width:58px;background:linear-gradient(#4aa3f0,var(--blue-dark))}
.auth.sign-up{left:814px;width:58px;background:linear-gradient(#ff9a3c,var(--orange-dark))}
.social{width:22px;height:22px;border:1.5px solid #777;border-radius:50%}

/* nav */
.main-nav{left:0;top:86px;width:1200px;height:52px;background:linear-gradient(#3a3a3a,#0d0d0d)}
.nav-list{left:227px;top:96px;display:flex;list-style:none;align-items:center}
.nav-list li{color:var(--white);font-size:15px;margin-right:22px;height:28px;line-height:28px}
.nav-list li.active{background:var(--orange);border-radius:14px;padding:0 12px;margin-right:22px}

/* side tabs */
.side-tab{left:1167px;width:33px;color:var(--white);font-size:11px;border-radius:6px 0 0 6px}
.side-tab span{position:absolute;left:10px;writing-mode:vertical-rl;transform:rotate(180deg)}
.tab-login{top:88px;height:142px;background:var(--blue)}
.tab-social{top:241px;height:144px;background:#111}

/* hero */
.hero{left:0;top:138px;width:1200px;height:320px;background:radial-gradient(circle at 70% 40%,#e8a878,#c3743f 45%,#8f4d24)}
.hero-title{left:0;top:202px;width:1200px;text-align:center;color:var(--white);font-size:54px;letter-spacing:1px}
.hero-pill{left:352px;top:273px;width:494px;height:54px;border-radius:27px;background:linear-gradient(#2a2a2a,#000);color:var(--white);font-size:54px;text-align:center;line-height:56px;box-shadow:0 2px 6px rgba(0,0,0,.5)}
.dot{top:421px;width:12px;height:12px;border-radius:50%;border:2px solid #f0d2bd}

/* intro */
.intro{left:0;top:458px;width:1200px;height:225px;background:var(--light)}
.intro-title{left:0;top:478px;width:1200px;text-align:center;font-size:24px;color:#333}
.intro-text{left:247px;top:515px;width:685px;font-size:11px;line-height:15.5px;color:#444}
.join-btn{left:493px;top:577px;width:205px;height:42px;border-radius:21px;background:linear-gradient(#555,#2c2c2c);color:var(--white);font-size:21px;text-align:center;line-height:42px}

/* partners */
.partners{left:232px;top:655px;width:725px;height:99px;background:linear-gradient(var(--white),#ececec);border:1px solid #dcdcdc;border-radius:4px}
.partners-label{left:458px;top:645px;width:300px;height:16px;background:var(--orange);color:var(--white);font-size:10.5px;text-align:center;line-height:16px}
.partner-row{left:258px;top:690px;width:660px;display:flex;justify-content:space-between;align-items:center}
.partner{font-size:20px;color:#8c8c8c}
.arrow-btn{top:727px;width:22px;height:22px;border-radius:50%;background:var(--white);border:1px solid #bbb}
.arrow-btn svg{display:block}

/* sections */
.section-title{top:790px;font-size:22px;color:#333}
.view-all{top:792px;width:66px;height:21px;border-radius:3px;background:linear-gradient(#3f9be8,var(--blue-dark));color:var(--white);font-size:11px;text-align:center;line-height:21px}
.date{left:259px;width:30px;height:28px;border:1.5px solid #444;text-align:center;font-size:13px;line-height:14px;padding-top:2px;color:#333}
.date small{display:block;font-size:5px;line-height:6px}
.news-text{left:310px;width:285px;font-size:9.5px;line-height:15.5px;color:#444}

/* testimonial speech bubbles */
.quote{left:630px;width:299px;height:72px;border:1px solid var(--card-line);border-radius:6px;background:var(--white);padding:9px 6px 0 13px;font-size:9px;letter-spacing:-0.15px;line-height:16px;color:#444;box-shadow:0 1px 3px rgba(0,0,0,.1)}
.quote p{white-space:nowrap}
.quote cite{position:absolute;left:13px;top:48px;font-style:normal;font-weight:bold;font-size:9.5px;color:var(--grey);font-family:Georgia,serif;letter-spacing:0}
.quote .tail{position:absolute;right:26px;bottom:-13px;display:block}

/* footer */
.site-footer{left:0;top:1033px;width:1200px;height:69px;background:linear-gradient(#3a3a3a,#1a1a1a)}
.footer-links{left:247px;top:1050px;font-size:9px;color:#aaa}
.copyright{left:247px;top:1070px;font-size:9px;color:#ddd}
.footer-social{top:1049px;width:21px;height:21px;border:1.5px solid #777;border-radius:50%}
.footer-brand{left:788px;top:1052px;display:flex;align-items:center;gap:7px}
.footer-brand .brand-mark{width:26px;height:26px;background:#aaa}
.footer-brand .brand-name{font-size:28px;color:#aaa}
</style>
</head>
<body>

<header class="abs site-header"></header>
<div class="abs brand"><span class="brand-mark"></span><span class="brand-name">Zyl Pando</span></div>
<div class="abs brand-tagline">EARN MONEY &amp; INCREASE SALES</div>
<div class="abs auth sign-in">Sign In</div>
<div class="abs auth sign-up">Sign Up</div>
<div class="abs social" style="left:887px;top:16px"></div>
<div class="abs social" style="left:919px;top:16px"></div>
<div class="abs social" style="left:951px;top:16px"></div>

<nav class="abs main-nav"></nav>
<ul class="abs nav-list">
  <li class="active">HOME</li><li>ABOUT US</li><li>OUR BLOG</li><li>TESTIMONIALS</li><li>AFFILIATES</li><li>ADVERTISERS</li><li>CONTACT US</li>
</ul>

<section class="abs hero" role="img" aria-label="Blurred orange-toned photograph of a busy shopping street"></section>
<h1 class="abs hero-title" style="font-weight:normal">EARN MONEY</h1>
<div class="abs hero-pill">&amp; INCREASE SALES</div>
<span class="abs dot" style="left:541px;background:#e04040"></span>
<span class="abs dot" style="left:578px;background:#3f8ee8"></span>
<span class="abs dot" style="left:616px;background:#5cb84a"></span>
<span class="abs dot" style="left:653px;background:#f2b21a"></span>

<div class="abs side-tab tab-login"><span style="top:10px">ACCOUNT LOGIN</span></div>
<div class="abs side-tab tab-social"><span style="top:12px">SOCIAL BAR</span>
  <svg class="abs" style="left:7px;top:107px" width="20" height="20" viewBox="0 0 20 20"><circle cx="10" cy="10" r="8.5" fill="none" stroke="#fff" stroke-width="1.5"/><path d="M10 5v10M5 10h10" stroke="#fff" stroke-width="1.5"/></svg>
</div>

<section class="abs intro"></section>
<h2 class="abs intro-title" style="font-weight:normal">Zyl Pando: International CPA Affiliate Network</h2>
<p class="abs intro-text">Welcome to the Zyl Pando affiliate network. On time payments, hot &amp; exclusive CPL/CPA offers, fast support and low fees for advertisers, is the making of a leading affiliate network!<br>Zyl Pando offer a wide range of advertisers for your websites. So you can start monetizing your traffic or get an additional revenue stream, today</p>
<div class="abs join-btn">JOIN US TODAY!</div>

<div class="abs partners"></div>
<div class="abs partners-label">USED BY THOUSANDS OF BIG SMALL BUSINESSES</div>
<div class="abs partner-row">
  <span class="partner">Quorix</span><span class="partner">Artvo</span><span class="partner">Pinwell</span><span class="partner">Hepta</span><span class="partner">Wirebox</span><span class="partner">Tedra</span><span class="partner">Fitlane</span><span class="partner">Tobo</span>
</div>
<div class="abs arrow-btn" style="left:238px"><svg width="20" height="20" viewBox="0 0 20 20"><path d="M12 6l-4 4 4 4" fill="none" stroke="#222" stroke-width="2"/></svg></div>
<div class="abs arrow-btn" style="left:928px"><svg width="20" height="20" viewBox="0 0 20 20"><path d="M8 6l4 4-4 4" fill="none" stroke="#222" stroke-width="2"/></svg></div>

<svg class="abs" style="left:259px;top:783px" width="40" height="38" viewBox="0 0 40 38"><rect x="1" y="1" width="36" height="35" fill="none" stroke="#555" stroke-width="2"/><rect x="6" y="6" width="9" height="9" fill="none" stroke="#555" stroke-width="1.5"/><path d="M18 8h15M18 13h15M6 19h27M6 24h27M6 29h27" stroke="#555" stroke-width="1.5"/></svg>
<h3 class="abs section-title" style="left:317px;font-weight:normal">NEWS / EVENT</h3>
<div class="abs view-all" style="left:511px">View All</div>

<svg class="abs" style="left:624px;top:783px" width="40" height="38" viewBox="0 0 40 38"><path d="M4 34l3-10L29 2l7 7-22 22z M7 24l7 7" fill="none" stroke="#555" stroke-width="2"/></svg>
<h3 class="abs section-title" style="left:672px;font-weight:normal">TESTIMONIALS</h3>
<div class="abs view-all" style="left:862px">View All</div>

<div class="abs date" style="top:850px">20<small>FEB</small></div>
<p class="abs news-text" style="top:849px;width:250px">Lorem ipsum dolor sit amet, consectetuer adipiscing elit, sed diam nonummy nibh euismod tincidunt ut laoreet dolore magna.</p>
<div class="abs date" style="top:904px">20<small>FEB</small></div>
<p class="abs news-text" style="top:903px">Lorem ipsum dolor sit amet, consectetuer adipiscing elit, sed diam nonummy nibh euismod tincidunt ut laoreet dolore magna.</p>
<div class="abs date" style="top:953px">20<small>FEB</small></div>
<p class="abs news-text" style="top:952px;width:255px">Lorem ipsum dolor sit amet, consectetuer adipiscing elit, sed diam nonummy nibh euismod tincidunt ut laoreet dolore magna.</p>

<blockquote class="abs quote" style="top:837px">
  <p>"Lorem ipsum dolor sit amet, consectetuer adipiscing elit, sed diam</p>
  <p>nonummy nibh euismod tincidunt ut laoreet dolore magna."</p>
  <cite>— Daniel Marsh</cite>
  <svg class="tail" width="22" height="14" viewBox="0 0 22 14"><path d="M1 0 Q8 6 3 13 Q14 10 20 0" fill="#fff" stroke="#dddddd" stroke-width="1"/><rect x="1.5" y="0" width="18" height="1.5" fill="#fff"/></svg>
</blockquote>
<blockquote class="abs quote" style="top:926px">
  <p>"Lorem ipsum dolor sit amet, consectetuer adipiscing elit, sed diam</p>
  <p>nonummy nibh euismod tincidunt ut laoreet dolore magna."</p>
  <cite>— Daniel Marsh</cite>
  <svg class="tail" width="22" height="14" viewBox="0 0 22 14"><path d="M1 0 Q8 6 3 13 Q14 10 20 0" fill="#fff" stroke="#dddddd" stroke-width="1"/><rect x="1.5" y="0" width="18" height="1.5" fill="#fff"/></svg>
</blockquote>

<footer class="abs site-footer"></footer>
<div class="abs footer-links">Affiliate Terms &amp; Conditions | advertiser Terms &amp; Conditions | privacy Policy &amp; Cookies | faq | contact Us</div>
<div class="abs copyright">© 2013 Pando Media UK Ltd - All Rights Reserved.</div>
<div class="abs footer-social" style="left:681px"></div>
<div class="abs footer-social" style="left:713px"></div>
<div class="abs footer-social" style="left:744px"></div>
<div class="abs footer-brand"><span class="brand-mark"></span><span class="brand-name">Zyl Pando</span></div>

</body>
</html>
```